Harrowgate Home Works Sales Flyer

We want a sales flyer that outlines our companies strengths with Kitchen & Bath Remodeling. We would like highlight those aspects while also showcasing our ability to do decks and home additions. We want financing packages to be a big part of the flyer.

Target Market(s)

Residential Customers

Requirements
Must have
• Financing options
Highlight Kitchen & bath remodeling
Less subtle is our decks and home additions
Nice to have
• Keep within our logo colors-we are looking for informative flyers that leave homeowners eager to call us after a meeting

```html
<!DOCTYPE html>
<html lang="en">
<head>
<meta charset="UTF-8">
<title>Harrowgate Home Works – Sales Flyer</title>
<link href="https://fonts.googleapis.com/css2?family=Poppins:wght@300;400;500;600;700&display=swap" rel="stylesheet">
<style>
  :root {
    --brand-blue: #1ba2d3;
    --white: #ffffff;
    --photo-light: #e9ecee;
    --photo-mid: #b9bfc4;
    --photo-dark: #6f767c;
  }
  * { margin: 0; padding: 0; box-sizing: border-box; }
  html, body { width: 927px; height: 1200px; overflow: hidden; background: var(--white); }
  body { font-family: "Poppins", sans-serif; color: var(--white); }
  .flyer { position: relative; width: 927px; height: 1200px; overflow: hidden; }
  .flyer-backdrop { position: absolute; inset: 0; }
  .headline {
    position: absolute; left: 103px; top: 48px; width: 380px;
    font-size: 55px; font-weight: 500; line-height: 70px; text-transform: uppercase;
  }
  .intro {
    position: absolute; left: 103px; top: 266px; width: 300px;
    font-size: 16.5px; font-weight: 300; line-height: 21px;
  }
  .service-list {
    position: absolute; left: 517px; top: 50px; list-style: none;
    font-size: 14.5px; font-weight: 300; line-height: 36.4px;
  }
  .contact {
    position: absolute; left: 68px; width: 336px; top: 886px; text-align: center;
  }
  .contact-label { font-size: 14.5px; font-weight: 300; line-height: 22px; }
  .contact-phone { font-size: 28px; font-weight: 600; line-height: 36px; }
  .contact-note { font-size: 14.5px; font-weight: 300; line-height: 22px; }
  .contact-web { font-size: 14.5px; font-weight: 400; line-height: 28px; }
  .brand {
    position: absolute; left: 68px; width: 336px; top: 1050px;
    display: flex; flex-direction: column; align-items: center; gap: 12px;
  }
  .brand-dot { width: 38px; height: 38px; border-radius: 50%; background: var(--white); }
  .brand-name { font-size: 24px; font-weight: 600; letter-spacing: 0.5px; }
  .other-services { position: absolute; left: 517px; top: 905px; width: 320px; }
  .other-title { font-size: 30px; font-weight: 500; line-height: 44px; margin-bottom: 6px; }
  .other-list { list-style: none; font-size: 14.5px; font-weight: 300; line-height: 34px; }
  .other-list .highlight { font-size: 17px; font-weight: 500; }
  .financing {
    margin-top: 10px; font-size: 23px; font-weight: 700; line-height: 30px;
    text-transform: uppercase; letter-spacing: 0.3px;
  }
</style>
</head>
<body>
<main class="flyer">
  <svg class="flyer-backdrop" width="927" height="1200" viewBox="0 0 927 1200">
    <defs>
      <linearGradient id="kitchenTones" x1="0" y1="0" x2="1" y2="1">
        <stop offset="0" stop-color="var(--photo-mid)"/>
        <stop offset="0.45" stop-color="var(--photo-light)"/>
        <stop offset="0.75" stop-color="var(--photo-mid)"/>
        <stop offset="1" stop-color="var(--photo-dark)"/>
      </linearGradient>
    </defs>
    <rect class="kitchen-photo" width="927" height="1200" fill="url(#kitchenTones)" role="img"
          aria-label="Photo of a bright open-plan kitchen with granite island, white cabinets and a living area with a stone fireplace"/>
    <polygon class="panel-top" points="68,0 859,0 859,455 68,553" fill="var(--brand-blue)"/>
    <polygon class="panel-bottom" points="68,795 859,712 859,1200 68,1200" fill="var(--brand-blue)"/>
  </svg>

  <h1 class="headline">It's time to make a change!</h1>
  <p class="intro">We specialize in updating and transforming kitchen areas. If you want to change the layout of your kitchen, expand into another room, or take down a wall to open the space, WE CAN DO IT.</p>

  <ul class="service-list">
    <li>- Open concept design services</li>
    <li>- Kitchen cabinet installation services</li>
    <li>- Kitchen countertop installation services</li>
    <li>- Tile installation services</li>
    <li>- Lighting installation services</li>
    <li>- Plumbing upgrade services</li>
    <li>- Electrical upgrade services</li>
    <li>- Drywall services</li>
    <li>- Painting services</li>
  </ul>

  <section class="contact">
    <p class="contact-label">Call us at</p>
    <p class="contact-phone">515-555-0148</p>
    <p class="contact-note">To get started on your project now</p>
    <p class="contact-web">https://harrowgatehomeworks.com</p>
  </section>

  <div class="brand">
    <span class="brand-dot"></span>
    <span class="brand-name">Harrowgate Home Works</span>
  </div>

  <section class="other-services">
    <h2 class="other-title">Other Services</h2>
    <ul class="other-list">
      <li class="highlight">- Bathroom remodeling</li>
      <li>- Kitchen cabinet installation services</li>
      <li class="highlight">- Decks/Patios</li>
      <li class="highlight">- Home additions</li>
    </ul>
    <p class="financing">Financing Options Available!</p>
  </section>
</main>
</body>
</html>
```